Vexor Ridge website

i'm looking for a promotional website for my business.
we provide Rope Access, Work at Height & Difficult Access services.
we treat water leak into buildings, external renovation of buildings, windows cleaning, confined spaces services and practically jobs in which the access is difficult.
here are examples of web site i like :
http://www.pixelbarnwebs.example/site-themes/51827.html
http://www.pixelbarnwebs.example/page-templates/62914.html

Target Market(s)

private people, commercial household chiefs, maintenance managers

Industry/Entity Type

Business

Requirements
Must have
• - mobile friendly
- chatterbay redirection
- 5 tabs
- one more customizable page - so i can add a photo and a description of the service corresponding (for now i offer 7 different services)
- contact us on each page with no redirection
- we are offering 7 different services
the website will be published in Israel which means right to left or centered for english option in the future. (logo on left hand corner)

- no flash
- should be future customisable - for future
Nice to have
• - a space for a slogan
- non scrollable
- photos on the landing page + redirection to gallery (photos and short films)
- 3 dynamic banners with short description of the theme of each, clicking on the banner after it opened will redirect to it's corresponding page.

```html
<!DOCTYPE html>
<html lang="en">
<head>
<meta charset="utf-8">
<title>Vexor Ridge — Rope Access &amp; Work at Height</title>
<link href="https://fonts.googleapis.com/css2?family=Open+Sans:wght@300;400;600;700&display=swap" rel="stylesheet">
<style>
:root{
  --black:#000;
  --white:#fff;
  --panel:#111112;
  --band:#e1e1e1;
  --band-dark:#bdbdbd;
  --muted:#777;
  --muted-dark:#555;
  --text-dark:#222;
  --footer-bar:#1b1b1f;
  --tab:#ececec;
  --tab-line:#c8c8c8;
}
*{margin:0;padding:0;box-sizing:border-box}
html,body{width:1148px;height:1200px;overflow:hidden;background:var(--black)}
body{font-family:"Open Sans",Arial,sans-serif;position:relative;color:var(--white)}
.abs{position:absolute}
.topbar{left:0;top:0;width:1148px;height:42px;background:var(--white)}
.hero{left:182px;top:42px;width:784px;height:362px;
  background:linear-gradient(180deg,rgba(0,0,0,0) 55%,#000 100%),
  linear-gradient(100deg,#cfcfcf 0%,#9aa4b4 18%,#2b4f94 40%,#3a66c2 60%,#2a4d98 78%,#d9d9d9 92%,#efefef 100%)}
.nav{left:294px;top:0;width:561px;height:105px;background:var(--white);box-shadow:0 3px 6px rgba(0,0,0,.35)}
.brand{left:0;top:0;width:161px;height:105px;display:flex;align-items:center;justify-content:center;gap:7px;
  font-size:17px;font-weight:700;color:var(--black);white-space:nowrap}
.brand-dot{width:12px;height:12px;border-radius:50%;background:var(--black)}
.tab-active{left:161px;top:0;width:76px;height:111px;background:var(--tab);border-bottom:10px solid var(--tab-line)}
.nav-item{top:68px;font-size:11px;font-weight:700;color:var(--black);transform:translateX(-50%);white-space:nowrap}
.dots{left:324px;top:429px;display:flex;gap:9px}
.dots span{width:7px;height:7px;border-radius:50%;background:var(--white)}
.services{left:294px;top:472px;width:561px;height:245px;background:var(--panel)}
.service{top:0;width:110px;transform:translateX(-50%);text-align:center}
.service-title{margin-top:27px;font-size:15px;font-weight:300;line-height:17px;color:var(--muted)}
.service.current .service-title,.service.current .view{color:var(--white)}
.service svg{display:block;margin:18px auto 0}
.view{margin-top:14px;font-size:10px;line-height:14px;color:var(--muted)}
.service svg.plus{margin:2px auto 0}
.band{left:0;top:733px;width:1148px;height:195px;background:var(--band)}
.band-slope{left:0;top:733px}
.work-title{left:301px;top:766px;width:180px;text-align:center;white-space:nowrap;
  font-size:16px;line-height:20px;font-weight:300;color:var(--text-dark)}
.work-rule{left:316px;top:790px;width:152px;height:1px;background:#9a9a9a}
.work-sub{left:301px;top:795px;width:180px;text-align:center;font-size:11px;line-height:14px;color:var(--text-dark)}
.work-text{left:306px;top:814px;width:170px;text-align:center;font-size:7.5px;line-height:9px;color:#888}
.btn{display:flex;align-items:center;justify-content:center;color:var(--white);
  background:linear-gradient(#2e2e2e,#111);font-size:10px}
.btn-details{left:316px;top:860px;width:151px;height:27px}
.equip-title{left:644px;top:758px;font-size:16px;color:#111;display:flex;align-items:center;gap:8px;white-space:nowrap}
.equip-title i{width:4px;height:4px;border-radius:50%;background:#555}
.thumb{top:798px;width:76px;height:76px;border-radius:5px;border:2px solid #9d9d9d}
.more{top:881px;width:76px;height:19px;background:#111;font-size:7px;font-weight:700;
  flex-direction:column;line-height:8px}
.more svg{display:block}
.footer-bar{left:0;top:1142px;width:1148px;height:58px;background:var(--footer-bar)}
.col-title{font-size:17px;font-weight:300;color:var(--white);white-space:nowrap}
.divider{top:951px;width:1px;height:162px;background:#1d1d1d}
.news{left:319px;top:992px;width:150px;list-style:none}
.news li{font-size:7.5px;line-height:9px;color:#ccc;padding-left:8px;position:relative;margin-bottom:7px}
.news li::before{content:"";position:absolute;left:0;top:3px;width:3px;height:3px;background:#ccc}
.caption{font-size:7px;line-height:9px;color:var(--muted-dark);text-transform:uppercase}
.faq-list{list-style:none;font-size:7.5px;color:#ccc}
.faq-list li{height:12.5px;padding-left:7px;position:relative;white-space:nowrap}
.faq-list li::before{content:"";position:absolute;left:0;top:3px;width:3px;height:3px;background:#ccc}
.btn-faq{left:512px;top:1078px;width:152px;height:29px;background:linear-gradient(#1a1a1a,#0a0a0a);font-size:10px}
.address{left:718px;top:1016px;font-size:10px;line-height:13px;color:var(--white)}
.email{left:756px;top:1077px;font-size:8px;color:var(--white);white-space:nowrap}
.copyright{left:322px;top:1165px;font-size:8px;color:var(--white);white-space:nowrap}
.social{top:1156px;width:24px;height:24px;border-radius:50%;background:#3c3c40}
</style>
</head>
<body>
<div class="abs topbar"></div>
<div class="abs hero" role="img" aria-label="Rope access technicians abseiling down the curved blue glass facade of a tall building"></div>

<header class="abs nav">
  <div class="abs brand"><span class="brand-dot"></span>Vexor Ridge</div>
  <div class="abs tab-active"></div>
  <a class="abs nav-item" style="left:198px">HOME</a>
  <a class="abs nav-item" style="left:279px">OUR STAFF</a>
  <a class="abs nav-item" style="left:360px">SERVICES</a>
  <a class="abs nav-item" style="left:433px">CONTACT</a>
  <a class="abs nav-item" style="left:511px">EQUIPMENTS</a>
</header>

<div class="abs dots"><span></span><span></span><span></span></div>

<section class="abs services">
  <div class="abs service current" style="left:63px">
    <div class="service-title">SERVICE<br>TYPE I</div>
    <svg width="80" height="90" viewBox="0 0 80 90" role="img" aria-label="Technician cleaning glass windows on a rope"><defs><linearGradient id="g1" x1="0" y1="0" x2="1" y2="1"><stop offset="0" stop-color="#bcd6f0"/><stop offset="1" stop-color="#3d7fcf"/></linearGradient></defs><polygon points="40,2 78,24 78,66 40,88 2,66 2,24" fill="url(#g1)" stroke="#333" stroke-width="2"/></svg>
    <div class="view">view more</div>
    <svg class="plus" width="12" height="12" viewBox="0 0 12 12"><circle cx="6" cy="6" r="5.3" fill="none" stroke="#fff" stroke-width=".8"/><path d="M6 3v6M3 6h6" stroke="#fff" stroke-width=".8"/></svg>
  </div>
  <div class="abs service" style="left:171px">
    <div class="service-title">SERVICE<br>TYPE II</div>
    <svg width="80" height="90" viewBox="0 0 80 90" role="img" aria-label="Worker inside industrial machinery"><defs><linearGradient id="g2" x1="0" y1="0" x2="1" y2="1"><stop offset="0" stop-color="#4d5b58"/><stop offset="1" stop-color="#1c2624"/></linearGradient></defs><polygon points="40,2 78,24 78,66 40,88 2,66 2,24" fill="url(#g2)" stroke="#333" stroke-width="2"/></svg>
    <div class="view">view more</div>
    <svg class="plus" width="12" height="12" viewBox="0 0 12 12"><circle cx="6" cy="6" r="5.3" fill="none" stroke="#777" stroke-width=".8"/><path d="M6 3v6M3 6h6" stroke="#777" stroke-width=".8"/></svg>
  </div>
  <div class="abs service" style="left:281px">
    <div class="service-title">SERVICE<br>TYPE III</div>
    <svg width="80" height="90" viewBox="0 0 80 90" role="img" aria-label="Technician working in a confined interior space"><defs><linearGradient id="g3" x1="0" y1="0" x2="1" y2="1"><stop offset="0" stop-color="#6a615b"/><stop offset="1" stop-color="#2d2826"/></linearGradient></defs><polygon points="40,2 78,24 78,66 40,88 2,66 2,24" fill="url(#g3)" stroke="#333" stroke-width="2"/></svg>
    <div class="view">view more</div>
    <svg class="plus" width="12" height="12" viewBox="0 0 12 12"><circle cx="6" cy="6" r="5.3" fill="none" stroke="#777" stroke-width=".8"/><path d="M6 3v6M3 6h6" stroke="#777" stroke-width=".8"/></svg>
  </div>
  <div class="abs service" style="left:390px">
    <div class="service-title">SERVICE<br>TYPE IV</div>
    <svg width="80" height="90" viewBox="0 0 80 90" role="img" aria-label="Rooftop view over a hazy city"><defs><linearGradient id="g4" x1="0" y1="0" x2="0" y2="1"><stop offset="0" stop-color="#8a8784"/><stop offset=".6" stop-color="#6f6a64"/><stop offset="1" stop-color="#5a4a38"/></linearGradient></defs><polygon points="40,2 78,24 78,66 40,88 2,66 2,24" fill="url(#g4)" stroke="#333" stroke-width="2"/></svg>
    <div class="view">view more</div>
    <svg class="plus" width="12" height="12" viewBox="0 0 12 12"><circle cx="6" cy="6" r="5.3" fill="none" stroke="#777" stroke-width=".8"/><path d="M6 3v6M3 6h6" stroke="#777" stroke-width=".8"/></svg>
  </div>
  <div class="abs service" style="left:499px">
    <div class="service-title">SERVICE<br>TYPE IV</div>
    <svg width="80" height="90" viewBox="0 0 80 90" role="img" aria-label="Rooftop view over a hazy city"><polygon points="40,2 78,24 78,66 40,88 2,66 2,24" fill="url(#g4)" stroke="#333" stroke-width="2"/></svg>
    <div class="view">view more</div>
    <svg class="plus" width="12" height="12" viewBox="0 0 12 12"><circle cx="6" cy="6" r="5.3" fill="none" stroke="#777" stroke-width=".8"/><path d="M6 3v6M3 6h6" stroke="#777" stroke-width=".8"/></svg>
  </div>
</section>

<div class="abs band"></div>
<svg class="abs band-slope" width="1148" height="195" viewBox="0 0 1148 195"><polygon points="586,0 855,0 855,195 515,195" fill="var(--band-dark)"/></svg>

<section>
  <h2 class="abs work-title">WORK THAT WE DO</h2>
  <div class="abs work-rule"></div>
  <h3 class="abs work-sub">SUBTITLE</h3>
  <p class="abs work-text">Missesma hasruane annitase. Mese feugie naseasetras strihaledaty ferian sit aerats laoisy ryatsras etasas jyatsrasa baystrasert.</p>
</section>
<a class="abs btn btn-details">VIEW DETAILS</a>

<div class="abs equip-title"><i></i>TOP EQUIPMENT</div>
<div class="abs thumb" style="left:580px;background:linear-gradient(135deg,#7d8fa3,#3b6aa0 50%,#a08060)" role="img" aria-label="Climber in harness on a steel frame"></div>
<div class="abs thumb" style="left:670px;background:linear-gradient(135deg,#d8d4cf,#9aa5ad 50%,#c9ced2)" role="img" aria-label="Worker adjusting rope gear"></div>
<div class="abs thumb" style="left:764px;background:linear-gradient(135deg,#c2703a,#8a4a2a 50%,#d78a45)" role="img" aria-label="Crew in orange suits with rescue equipment"></div>
<a class="abs btn more" style="left:580px">MORE<svg width="6" height="4" viewBox="0 0 6 4"><path d="M0 0h6L3 4z" fill="#fff"/></svg></a>
<a class="abs btn more" style="left:670px">MORE<svg width="6" height="4" viewBox="0 0 6 4"><path d="M0 0h6L3 4z" fill="#fff"/></svg></a>
<a class="abs btn more" style="left:764px">MORE<svg width="6" height="4" viewBox="0 0 6 4"><path d="M0 0h6L3 4z" fill="#fff"/></svg></a>

<footer>
  <h4 class="abs col-title" style="left:315px;top:960px">LATEST NEWS</h4>
  <ul class="abs news">
    <li>Lorem ipsum dolor sit amet, consectetur adipiscing elit. Sed blandit...</li>
    <li>Lorem ipsum dolor sit amet, consectetur adipiscing elit. Sed blandit...</li>
    <li>Lorem ipsum dolor sit amet, consectetur adipiscing elit. Sed blandit...</li>
    <li>Lorem ipsum dolor sit amet, consectetur adipiscing elit. Sed blandit...</li>
  </ul>
  <div class="abs divider" style="left:477px"></div>

  <h4 class="abs col-title" style="left:511px;top:960px">FAQ</h4>
  <p class="abs caption" style="left:512px;top:990px;width:155px">Beraertyasear niasesa resterigas eas nytrasas lasteas:</p>
  <ul class="abs faq-list" style="left:519px;top:1024px"><li>1. Question one</li><li>1. Question one</li><li>1. Question one</li></ul>
  <ul class="abs faq-list" style="left:595px;top:1024px"><li>1. Question one</li><li>1. Question one</li><li>1. Question one</li></ul>
  <a class="abs btn btn-faq">MORE</a>
  <div class="abs divider" style="left:691px"></div>

  <h4 class="abs col-title" style="left:718px;top:960px">CONTACT</h4>
  <p class="abs caption" style="left:719px;top:989px">Vexor Ridge office</p>
  <p class="abs address">48 Harlow Quay Rd<br>Port Elden<br>CA 90412</p>
  <svg class="abs" style="left:720px;top:1074px" width="24" height="17" viewBox="0 0 24 17"><rect width="24" height="17" fill="#fff"/><path d="M1 1l11 8 11-8" fill="none" stroke="#999" stroke-width="1"/></svg>
  <p class="abs email">info@vexorridge.example</p>

  <div class="abs footer-bar"></div>
  <p class="abs copyright">VEXOR RIDGE © 2013 PRIVACY POLICY</p>
  <a class="abs social" style="left:681px" aria-label="Plusring"></a>
  <a class="abs social" style="left:722px" aria-label="chatterbay"></a>
  <a class="abs social" style="left:762px" aria-label="News feed"></a>
  <a class="abs social" style="left:807px" aria-label="Chirpline"></a>
</footer>
</body>
</html>
```